update of B2B website and conversion to single page

The current website needs to be modernized. I want what is commonly called a single page website. It is not actually a single page. See some examples here:
https://www.brivolane.example/
https://www.quenzo.example/
https://www.tarnwickhub.example/
Most or all graphics will be replaced.
Please see the attached spreadsheet for a rough draft of the home page layout. Convert the existing website at https://www.zorbilinfo.example/ to a single page website. We will provide the page content. You will provide all of the design, graphics, development, production deployment. etc. The look and feel should be corporate, polished, premium.

```html
<!DOCTYPE html>
<html lang="en">
<head>
<meta charset="utf-8">
<title>Zorbil Data – Enterprise Data Quality</title>
<link href="https://fonts.googleapis.com/css2?family=Poppins:wght@300;400;500;600;700&display=swap" rel="stylesheet">
<style>
:root{
  --blue:#0a6fa6;
  --blue-dark:#065a88;
  --blue-deep:#04507a;
  --accent:#1a9ad6;
  --yellow:#f5c12e;
  --ink:#222;
  --muted:#777;
  --grey-bg:#f4f4f4;
  --pale:#f1f5fb;
  --green:#8aa860;
  --tan:#b09a63;
  --purple:#b463b5;
  --teal:#6ecbd1;
  --violet:#3a2a9e;
  --footer:#111;
  --footer-bar:#1c1c1c;
  --white:#fff;
}
*{margin:0;padding:0;box-sizing:border-box}
html,body{width:1200px;height:3965px;overflow:hidden}
body{font-family:'Poppins',sans-serif;color:var(--ink);position:relative;background:var(--white)}
.abs{position:absolute}
p{font-size:11px;line-height:1.75;color:var(--muted)}
.btn{position:absolute;display:flex;align-items:center;justify-content:center;font-size:10px;font-weight:600;letter-spacing:1.5px;text-transform:uppercase}
.more{font-size:9px;font-weight:600;letter-spacing:1.2px;color:var(--ink);text-transform:uppercase}

/* header + hero */
.hero{left:0;top:0;width:1200px;height:714px;background:linear-gradient(180deg,#0b72aa,#0a6aa0)}
.brand{left:30px;top:22px;display:flex;align-items:center;gap:10px;color:var(--white)}
.brand-mark{width:26px;height:26px;border-radius:50%;background:var(--yellow)}
.brand-name{font-size:22px;font-weight:700;line-height:1}
.brand-tag{font-size:8px;color:var(--white);opacity:.85;margin-top:2px}
.nav{right:50px;top:38px;display:flex;gap:44px}
.nav a{color:var(--white);text-decoration:none;font-size:11px;font-weight:500;letter-spacing:1.2px;text-transform:uppercase}
.hero-title{left:71px;top:215px;font-size:46px;font-weight:400;line-height:1.15;color:var(--yellow)}
.hero-lead{left:71px;top:342px;width:460px;color:var(--white)}
.hero-lead strong{display:block;font-size:12px;font-weight:600;margin-bottom:2px}
.hero-lead span{font-size:12px;line-height:1.6}
.hero-btn{left:74px;top:442px;width:120px;height:28px;border:1px solid rgba(255,255,255,.8);color:var(--white)}
.hero-art{left:648px;top:195px;width:470px;height:430px;border-radius:46% 46% 30% 30%;background:radial-gradient(circle at 45% 40%,#e8f1ff,#9fc0f2 60%,#3f6fd6)}

/* enterprise */
.enterprise{left:79px;top:655px;width:476px;height:408px;background:linear-gradient(160deg,#1483bc,#0a5c8e);border:10px solid var(--white);outline:1px solid #dfe7ee}
.enterprise h2{position:absolute;left:50px;top:100px;font-size:27px;font-weight:400;color:var(--white);line-height:1.25}
.enterprise p{position:absolute;left:50px;top:185px;width:360px;color:rgba(255,255,255,.85);font-size:10.5px}
.enterprise .btn{left:52px;top:272px;width:106px;height:26px;background:var(--white);color:var(--blue)}
.conn{left:680px;width:300px}
.conn h4{font-size:10.5px;font-weight:600;letter-spacing:1px;text-transform:uppercase;display:flex;align-items:center;gap:10px}
.conn .ic{width:18px;height:16px;border:1.5px solid #555;border-radius:2px}
.conn p{margin:4px 0 0 28px;font-size:10px}
.conn-line{left:600px;top:822px;width:70px;height:1px;background:#ccc}

/* apps */
.apps-title{left:222px;top:1160px;font-size:30px;font-weight:400;line-height:1.15;color:var(--ink)}
.apps-title em{font-style:normal;color:var(--accent)}
.app{left:222px;width:370px}
.app h4{font-size:11px;font-weight:600;display:flex;align-items:center;gap:10px}
.app .ic{width:16px;height:16px;border:1.5px solid #444;border-radius:3px}
.app p{margin:6px 0 8px 26px;font-size:10px}
.app .more{margin-left:26px}
.diagram{left:646px;top:1142px;width:456px;height:456px;border-radius:50%;border:2px solid #e6e6e6;background:radial-gradient(circle at 50% 55%,#cfe0f4 0%,#eef4fb 55%,#fff 75%)}

/* trial band */
.trial{left:0;top:1694px;width:1200px;height:249px;background:linear-gradient(100deg,#5c7388 0%,#7a8da0 45%,#a99aa0 75%,#c4a3a2 100%)}
.trial h2{position:absolute;left:0;right:0;top:80px;text-align:center;color:var(--white);font-size:27px;font-weight:600}
.trial .btn{left:560px;top:142px;width:124px;height:30px;background:var(--white);color:var(--blue)}

/* why */
.why-panel{left:682px;top:1946px;width:381px;height:446px;background:var(--pale)}
.why-photo{left:92px;top:2009px;width:423px;height:330px;background:linear-gradient(160deg,#f3f3f3,#c9a57c 55%,#2f2f2f)}
.why-title{left:603px;top:2030px;font-size:28px;font-weight:400}
.why-title em{font-style:normal;color:var(--accent)}
.why-item{left:603px;width:390px}
.why-item h4{font-size:13px;font-weight:600}
.why-item p{font-size:10px;margin:6px 0 8px}

/* services */
.services{left:0;top:2397px;width:1200px;height:537px;background:var(--grey-bg)}
.svc-mark{left:588px;top:2428px;width:24px}
.svc-title{left:0;right:0;top:2490px;text-align:center;font-size:27px;font-weight:400;letter-spacing:.5px}
.svc-lead{left:330px;top:2540px;width:540px;text-align:center;font-size:10px}
.card{top:2609px;width:259px;height:259px;display:flex;flex-direction:column;align-items:center;justify-content:center;color:var(--white)}
.card .circle{width:110px;height:110px;border-radius:50%;border:2px solid var(--white);display:flex;align-items:center;justify-content:center;margin-bottom:20px}
.card h3{font-size:24px;font-weight:700}
.arrow-btn{top:2702px;width:28px;height:46px;background:#1c1c1c;display:flex;align-items:center;justify-content:center}

/* testimonials */
.testi{left:0;top:2934px;width:1200px;height:357px;background:linear-gradient(90deg,#1278b0,#0a6aa0 55%,#0b6fa6)}
.testi-left{left:0;top:0;width:565px;height:357px;background:rgba(255,255,255,.06)}
.testi-icon{left:230px;top:3057px;width:30px;height:26px;border:1.5px solid var(--white);border-radius:3px}
.testi-title{left:120px;top:3104px;width:250px;text-align:center;color:var(--white);font-size:22px;font-weight:400;line-height:1.2}
.quote{left:568px;top:3008px;width:431px;height:217px;background:#f2f2f2;border-radius:2px;padding:50px 45px 0;text-align:center}
.quote p{font-size:13px;color:#666;line-height:1.6;font-weight:300}
.quote strong{display:block;margin-top:14px;font-size:10px;color:var(--accent);letter-spacing:1px;font-weight:600;text-transform:uppercase}
.quote small{font-size:8px;color:#999}
.quote-tip{left:556px;top:3105px;width:0;height:0;border-top:12px solid transparent;border-bottom:12px solid transparent;border-right:12px solid #f2f2f2}
.dot{width:7px;height:7px;border-radius:50%;background:var(--white)}

/* work + newsletter */
.work{left:0;top:3291px;width:608px;height:317px;background:linear-gradient(120deg,#3a1e92,#4b2cc0 55%,#2f3fbf)}
.work h2{position:absolute;left:0;right:0;top:80px;text-align:center;color:var(--white);font-size:27px;font-weight:400}
.work p{position:absolute;left:30px;width:548px;top:138px;text-align:center;color:rgba(255,255,255,.9);font-size:11px}
.work .btn{left:244px;top:202px;width:120px;height:26px;border:1px solid var(--white);color:var(--white)}
.news h2{position:absolute;left:608px;width:592px;top:3371px;text-align:center;font-size:27px;font-weight:400}
.news-input{left:772px;top:3429px;width:358px;height:34px;border:1px solid #ddd;display:flex;align-items:center;justify-content:center;font-size:9px;letter-spacing:1.5px;color:#444}
.news .btn{left:890px;top:3485px;width:122px;height:28px;background:var(--accent);color:var(--white)}

/* footer */
.footer{left:0;top:3608px;width:1200px;height:283px;background:var(--footer)}
.f-brand{left:68px;top:3640px}
.f-about{left:68px;top:3717px;width:250px;color:#bbb;font-size:10px}
.f-col{top:3680px;color:var(--white)}
.f-col h5{font-size:10px;font-weight:600;letter-spacing:1.5px;margin-bottom:18px;text-transform:uppercase}
.f-col li{list-style:none;font-size:10.5px;color:#bbb;line-height:2}
.f-contact li{display:flex;gap:8px;align-items:flex-start;line-height:1.6;margin-bottom:8px}
.f-contact .ic{flex:none;width:10px;height:10px;border:1px solid #bbb;border-radius:2px;margin-top:3px}
.socials{display:flex;gap:14px;margin-top:6px}
.socials span{width:12px;height:12px;border-radius:50%;background:var(--accent)}
.f-bar{left:0;top:3891px;width:1200px;height:74px;background:var(--footer-bar)}
.f-bar p{position:absolute;left:74px;top:28px;font-size:9px;color:#888}
</style>
</head>
<body>

<!-- HERO -->
<section class="abs hero"></section>
<div class="abs brand">
  <span class="brand-mark"></span>
  <div><div class="brand-name">Zorbil Data</div><div class="brand-tag">Enterprise Data Quality Made Easy</div></div>
</div>
<nav class="abs nav">
  <a>Services</a><a>Connectors</a><a>Features</a><a>Why QV Plus?</a><a>Offers</a><a>Blog</a><a>Company</a>
</nav>
<h1 class="abs hero-title">Data Quality Proof<br>of Concept</h1>
<div class="abs hero-lead">
  <strong>Find Out Exactly What QV Plus Can Do For You</strong>
  <span>Test drive QV Plus to cleanse data, verify addresses and positively identify duplicate records in your application or database.</span>
</div>
<div class="btn hero-btn">Full Features</div>
<div class="abs hero-art" role="img" aria-label="Illustration of a cloud holding server racks with a person standing beside them"></div>

<!-- ENTERPRISE -->
<section class="abs enterprise">
  <h2>Enterprise Data Quality<br>Made Easy</h2>
  <p>Cleanse data, verify addresses, find and consolidate duplicate records in batch and real time. Connectors for Orvane Business Suite, Tarnwick and Sorrel.</p>
  <div class="btn">Read More</div>
</section>
<div class="abs conn-line"></div>
<div class="abs conn" style="top:810px">
  <h4><span class="ic"></span>Orvane</h4>
  <p>QV Plus has connectors for all of the major SQL/relational databases, including Orvane. The QV Plus Orvane Database Connector eliminates the</p>
</div>
<div class="abs conn" style="top:915px">
  <h4><span class="ic" style="border-radius:50%"></span>NimbleSQL</h4>
  <p>The QV Plus Halcyon SQL Server Database Connector eliminates the need for custom integration work, saving your business time and</p>
</div>

<!-- APPLICATIONS -->
<h2 class="abs apps-title">We provdide <em>effective</em><br>Applications solutions</h2>
<div class="abs app" style="top:1265px">
  <h4><span class="ic"></span>Tarnwick, Sorrel</h4>
  <p>QV Plus makes it easy to cleanse data and consolidate duplicate records in Tarnwick.example. The QV Plus Tarnwick Connector eliminates integration work and</p>
  <span class="more">Read More ›</span>
</div>
<div class="abs app" style="top:1407px">
  <h4><span class="ic" style="border-radius:50%"></span>ServiceLoom, Orvane Business Suite</h4>
  <p>Orvane Applications, Orvane ERP, Orvane Financials. Regardless of what you call them, QV Plus can cleanse the data and merge duplicate records in your Orvane Business Suite.</p>
  <span class="more">Read More ›</span>
</div>
<div class="abs diagram" role="img" aria-label="Illustration of the product feeding an application tier database, with a document and a database stack"></div>

<!-- TRIAL BAND -->
<section class="abs trial" role="img" aria-label="Soft blurred office photograph behind the banner">
  <h2>Address Correction and Validation Free Trial</h2>
  <div class="btn">Free Trail</div>
</section>

<!-- WHY -->
<div class="abs why-panel"></div>
<div class="abs why-photo" role="img" aria-label="Photograph of a desk with a lamp, monitor, plant and a black chair"></div>
<h2 class="abs why-title">Why <em>QV Plus?</em></h2>
<div class="abs why-item" style="top:2084px">
  <h4>Designed for the Business User</h4>
  <p>A key goal of the QV Plus product design was elimination of the frustrating complexities common to most enterprise applications. Further, several features were developed to greatly accelerate the processes that take you from integration to deployment.</p>
  <span class="more">Read More ›</span>
</div>
<div class="abs why-item" style="top:2227px">
  <h4>Built for Speed</h4>
  <p>QV Plus was developed on the Kestrel EE platform ensuring maximum scalability. Application metadata is stored in the QV Plus database, transaction management and distributed computing are handled by the QV Plus.</p>
  <span class="more">Read More ›</span>
</div>

<!-- SERVICES -->
<section class="abs services"></section>
<svg class="abs svc-mark" viewBox="0 0 24 12"><line x1="0" y1="2" x2="24" y2="2" stroke="#1a9ad6" stroke-width="2"/><line x1="5" y1="8" x2="19" y2="8" stroke="#1a9ad6" stroke-width="2"/></svg>
<h2 class="abs svc-title">OUR SERVICES</h2>
<p class="abs svc-lead">Lorem ipsum dolor sit amet, consectetuer adipiscing elit, sed diam nonummy nibh euis mod tincidunt ut laoreet dolore mag na aliq uam erat volutpat.</p>

<div class="abs card" style="left:58px;background:var(--green)">
  <div class="circle"><svg width="46" height="50" viewBox="0 0 46 50" fill="none" stroke="#fff" stroke-width="2.5"><ellipse cx="23" cy="8" rx="20" ry="6"/><path d="M3 8v34c0 3.3 9 6 20 6s20-2.7 20-6V8"/><path d="M3 20c0 3.3 9 6 20 6s20-2.7 20-6M3 31c0 3.3 9 6 20 6s20-2.7 20-6"/></svg></div>
  <h3>Sorrel</h3>
</div>
<div class="abs card" style="left:336px;background:var(--tan)">
  <div class="circle"><svg width="50" height="50" viewBox="0 0 50 50" fill="none" stroke="#fff" stroke-width="2.5"><rect x="4" y="4" width="30" height="42"/><path d="M22 25h24M38 17l8 8-8 8"/></svg></div>
  <h3>Data Migration</h3>
</div>
<div class="abs card" style="left:613px;background:var(--purple)">
  <div class="circle"><svg width="54" height="46" viewBox="0 0 54 46" fill="none" stroke="#fff" stroke-width="2.5"><rect x="3" y="3" width="48" height="32" rx="2"/><path d="M18 43h18M27 35v8M10 26l10-9 8 6 14-13"/></svg></div>
  <h3>Data Quality</h3>
</div>
<div class="abs card" style="left:891px;background:var(--teal)">
  <div class="circle"><svg width="54" height="46" viewBox="0 0 54 46" fill="none" stroke="#fff" stroke-width="2.5"><rect x="3" y="6" width="42" height="28" rx="2"/><path d="M14 42h20M24 34v8"/><circle cx="45" cy="8" r="6"/></svg></div>
  <h3>Data Integration</h3>
</div>
<div class="abs arrow-btn" style="left:40px"><svg width="10" height="14" viewBox="0 0 10 14"><path d="M8 1 2 7l6 6" fill="none" stroke="#fff" stroke-width="2"/></svg></div>
<div class="abs arrow-btn" style="left:1137px"><svg width="10" height="14" viewBox="0 0 10 14"><path d="M2 1l6 6-6 6" fill="none" stroke="#fff" stroke-width="2"/></svg></div>

<!-- TESTIMONIALS -->
<section class="abs testi"><div class="abs testi-left" role="img" aria-label="Faint pattern of technology line icons"></div></section>
<div class="abs testi-icon"></div>
<h2 class="abs testi-title">What our clients<br>talk about us?</h2>
<div class="abs quote-tip"></div>
<div class="abs quote">
  <p>"Lorem ipsum dolor sit amet, consect etuer adipiscing elit, sed diam nonummy nibh euismod tincidunt ut laoreet dolore mag na aliquam."</p>
  <strong>Mirela Tosk</strong>
  <small>Designation</small>
</div>
<div class="abs dot" style="left:1017px;top:3113px"></div>

<!-- WORK + NEWSLETTER -->
<section class="abs work" role="img" aria-label="Isometric illustration of a purple digital city">
  <h2>Work with us?</h2>
  <p>Lorem ipsum dolor sit amet, consectetuer adipiscing elit. Aenean commodo ligula eget dolor. Aenean massa. Cum sociis natoque penatibus.</p>
  <div class="btn">Contact Us Now</div>
</section>
<section class="news">
  <h2>Stay up-to-date</h2>
  <div class="abs news-input">YOUR E-MAIL</div>
  <div class="btn">Subscribe Now</div>
</section>

<!-- FOOTER -->
<footer class="abs footer"></footer>
<div class="abs brand f-brand">
  <span class="brand-mark"></span>
  <div><div class="brand-name">Zorbil Data</div><div class="brand-tag">Enterprise Data Quality Made Easy</div></div>
</div>
<p class="abs f-about">Zorbil Data was founded in 1999 as a consulting company focused on the implementation of enterprise applications. Our team was comprised of senior software developers who had worked for many of the leading commercial application vendors.</p>
<div class="abs f-col" style="left:714px">
  <h5>About Us</h5>
  <ul><li>Services</li><li>Connectors</li><li>Features</li><li>Why QV Plus?</li><li>Offers</li><li>Blog</li><li>Company</li></ul>
</div>
<div class="abs f-col f-contact" style="left:928px;width:220px">
  <h5>Talk To Us</h5>
  <ul>
    <li><span class="ic"></span>(555) 013-2284</li>
    <li><span class="ic"></span>sales@zorbilinfo.example</li>
    <li><span class="ic"></span>Zorbil Data 88 Lindqvist Row Suite 4, Harrowvale, ST 00421</li>
  </ul>
  <div class="socials"><span></span><span></span><span></span><span></span><span></span></div>
</div>
<div class="abs f-bar"><p>© zorbilinfo.example. All Right Reserved 2020</p></div>

</body>
</html>
```